Corporate business card

Business card design for IT consultancy company.
Clients are larger companies.
Card should have round edges on some or all.
Make the user stop and look at the card.
Steel grey background. But if you have a better idea, show me.
Target Market(s)
Corporate - a but web 2.0
Industry/Entity Type
Business
Contact Information for Business Card
As per design.
Font styles to use
Other font styles liked:
- Helvetica
Colors
5c5c5c
ec2027
ffffff
Requirements
Must have
- Clean design - follow brivo styles
- text in white
- Lets have a conversation in red
- Powered by passion in red
Nice to have
- Uncluttered
Should not have
- Cluttered

```html
<!DOCTYPE html>
<html lang="en">
<head>
<meta charset="utf-8">
<title>Kestrel Strategy – Business Card</title>
<link rel="stylesheet" href="https://fonts.googleapis.com/css2?family=Open+Sans:wght@400;600;700;800&display=swap">
<style>
  :root {
    --page: #ffffff;
    --steel-light: #a3a5a8;
    --steel-mid: #8c8f92;
    --steel-dark: #76797c;
    --brand-red: #ec2027;
    --deep-red: #b3141a;
    --white: #ffffff;
    --ink-grey: #5c5c5c;
    --ghost: rgba(60, 62, 64, 0.16);
  }
  * { box-sizing: border-box; margin: 0; padding: 0; }
  html, body {
    width: 1200px;
    height: 900px;
    overflow: hidden;
    background: var(--page);
    font-family: "Open Sans", Helvetica, Arial, sans-serif;
  }
  .canvas {
    position: relative;
    width: 1200px;
    height: 900px;
  }
  .card {
    position: absolute;
    top: 291px;
    width: 520px;
    height: 318px;
    border-radius: 26px;
    overflow: hidden;
    background:
      linear-gradient(180deg, rgba(255,255,255,0.10) 0%, rgba(255,255,255,0) 40%, rgba(0,0,0,0.08) 100%),
      linear-gradient(100deg, var(--steel-light) 0%, var(--steel-mid) 55%, var(--steel-dark) 100%);
    box-shadow: 0 14px 30px rgba(0,0,0,0.18);
  }
  .card--front { left: 60px; }
  .card--back  { left: 620px; }

  /* Front */
  .brand-name {
    position: absolute;
    top: 34px;
    left: 0;
    width: 100%;
    text-align: center;
    color: var(--brand-red);
    font-weight: 800;
    line-height: 1;
  }
  .brand-name__main {
    display: block;
    font-size: 62px;
    letter-spacing: 2px;
  }
  .brand-name__sub {
    display: block;
    margin-top: 8px;
    font-size: 28px;
    letter-spacing: 6px;
  }
  .brand-rule {
    position: absolute;
    top: 160px;
    left: 0;
    width: 100%;
    height: 6px;
    background: linear-gradient(180deg, var(--brand-red) 0%, var(--deep-red) 100%);
    box-shadow: 0 2px 2px rgba(0,0,0,0.2);
  }
  .holder {
    position: absolute;
    top: 184px;
    left: 20px;
    width: 172px;
    text-align: right;
  }
  .holder__name {
    color: var(--brand-red);
    font-weight: 700;
    font-size: 14px;
    letter-spacing: 0.2px;
  }
  .holder__role {
    color: var(--white);
    font-size: 12.5px;
    margin-top: 1px;
  }
  .divider {
    position: absolute;
    top: 180px;
    left: 207px;
    width: 1px;
    height: 94px;
    background: rgba(255,255,255,0.75);
  }
  .contacts {
    position: absolute;
    top: 180px;
    left: 220px;
    list-style: none;
  }
  .contacts__item {
    display: flex;
    align-items: center;
    height: 18.5px;
    color: var(--white);
    font-size: 14.5px;
  }
  .contacts__icon {
    width: 12px;
    height: 12px;
    margin-right: 9px;
    flex: none;
  }
  .tagline {
    position: absolute;
    left: 24px;
    top: 282px;
    color: var(--brand-red);
    font-size: 12px;
    font-weight: 600;
    letter-spacing: 9.6px;
    white-space: nowrap;
  }

  /* Back */
  .ghost-name {
    position: absolute;
    top: 22px;
    left: 8px;
    color: var(--ghost);
    font-weight: 800;
    line-height: 1;
    white-space: nowrap;
  }
  .ghost-name__main {
    display: block;
    font-size: 132px;
    letter-spacing: 2px;
  }
  .ghost-name__sub {
    display: block;
    margin-top: 12px;
    font-size: 62px;
    letter-spacing: 14px;
  }
  .motto {
    position: absolute;
    top: 142px;
    left: 0;
    width: 100%;
    text-align: center;
    color: var(--brand-red);
    font-size: 15px;
    font-weight: 600;
    letter-spacing: 10px;
    white-space: nowrap;
  }
</style>
</head>
<body>
<main class="canvas">

  <section class="card card--front" aria-label="Card front">
    <h1 class="brand-name">
      <span class="brand-name__main">KESTREL</span>
      <span class="brand-name__sub">STRATEGY</span>
    </h1>
    <div class="brand-rule"></div>

    <div class="holder">
      <p class="holder__name">DANIEL HARWOOD</p>
      <p class="holder__role">MANAGING PARTNER</p>
    </div>

    <div class="divider"></div>

    <ul class="contacts">
      <li class="contacts__item">
        <svg class="contacts__icon" viewBox="0 0 12 12" aria-hidden="true">
          <path d="M2.2 1 L4.2 1 L5 3.4 L3.8 4.4 Q4.8 6.6 7.4 8.2 L8.5 7 L11 7.8 L11 9.8 Q10.6 11 9.4 11 Q4.8 10.6 1.6 6.4 Q1 4 1 2.4 Q1 1.2 2.2 1 Z" fill="var(--brand-red)"/>
        </svg>
        +61390471186
      </li>
      <li class="contacts__item">
        <svg class="contacts__icon" viewBox="0 0 12 12" aria-hidden="true">
          <rect x="3" y="0.5" width="6.5" height="11" rx="1" fill="var(--brand-red)"/>
          <rect x="4" y="1.8" width="4.5" height="6" fill="var(--steel-mid)"/>
        </svg>
        0400782514
      </li>
      <li class="contacts__item">
        <svg class="contacts__icon" viewBox="0 0 12 12" aria-hidden="true">
          <rect x="0.5" y="2.5" width="11" height="7.5" rx="1" fill="var(--brand-red)"/>
          <path d="M1 3 L6 7 L11 3" fill="none" stroke="var(--white)" stroke-width="1"/>
        </svg>
        daniel@kestrelstrategy.com.au
      </li>
      <li class="contacts__item">
        <svg class="contacts__icon" viewBox="0 0 12 12" aria-hidden="true">
          <circle cx="6" cy="6" r="5.5" fill="var(--brand-red)"/>
        </svg>
        daniel-harwood
      </li>
      <li class="contacts__item">
        <svg class="contacts__icon" viewBox="0 0 12 12" aria-hidden="true">
          <circle cx="6" cy="6" r="5.2" fill="none" stroke="var(--brand-red)" stroke-width="1.2"/>
          <ellipse cx="6" cy="6" rx="2.2" ry="5.2" fill="none" stroke="var(--brand-red)" stroke-width="1"/>
          <line x1="0.8" y1="6" x2="11.2" y2="6" stroke="var(--brand-red)" stroke-width="1"/>
        </svg>
        www.kestrelstrategy.com.au
      </li>
    </ul>

    <p class="tagline">LETS HAVE A CONVERSATION!</p>
  </section>

  <section class="card card--back" aria-label="Card back">
    <div class="ghost-name" aria-hidden="true">
      <span class="ghost-name__main">KESTREL</span>
      <span class="ghost-name__sub">STRATEGY</span>
    </div>
    <p class="motto">POWERED BY PASSION!</p>
  </section>

</main>
</body>
</html>
```